Buff & Gleam

polished concrete and epoxy coatings flooring company

Target Market(s)

Industrial commercial

Industry/Entity Type

Industrial flooring contractor

Contact Information for Business Card

POLISHED CONCRETE • EPOXY COATING • TERRAZZO RESTORATION • SHOT BLASTING • SURFACE PREPARATION • JOINT FILLING • TILE/ CARPET /GLUE REMOVAL

Colors
0054AA
0677BA
7BADD7
CADEEF
E8F1F8

Requirements
Must have
• email buffandgleamfloors@mailbrook.example Address 47215 Tallowmere Rd, Fraser, MI 48093. Name Ray Tulvin. Services Polished concrete- Epoxy Coatings- Terrazzo restoration-surface preparation- safety striping- joint filling- tile/ carpet/ glue removal phone number 586-700-3926 email buffandgleamfloors.example
Nice to have
• Instagram Facebook logo maybe smaller in the corner

```html
<!DOCTYPE html>
<html lang="en">
<head>
<meta charset="utf-8">
<title>Buff &amp; Gleam — Business Card</title>
<link href="https://fonts.googleapis.com/css2?family=Montserrat:wght@600;700;800&display=swap" rel="stylesheet">
<style>
  :root {
    --page: #ffffff;
    --card-base: #000000;
    --blue-deep: #0054AA;
    --blue-mid: #0677BA;
    --blue-soft: #7BADD7;
    --blue-pale: #CADEEF;
    --blue-mist: #E8F1F8;
    --sheen-shadow: #021a33;
    --ink: #ffffff;
    --rule: #7BADD7;
  }
  html, body {
    margin: 0;
    width: 1200px;
    height: 1200px;
    overflow: hidden;
    background: var(--page);
    font-family: "Montserrat", Arial, sans-serif;
  }
  .canvas {
    position: relative;
    width: 1200px;
    height: 1200px;
  }
  .card {
    position: absolute;
    left: 316px;
    width: 567px;
    height: 321px;
    background: var(--card-base);
    overflow: hidden;
    color: var(--ink);
  }
  .card--front { top: 265px; }
  .card--back  { top: 613px; }
  .card__sheen {
    position: absolute;
    inset: 0;
    width: 100%;
    height: 100%;
  }
  .brand {
    position: absolute;
    margin: 0;
    line-height: 1;
  }
  .brand__name {
    display: block;
    font-weight: 800;
    letter-spacing: -0.5px;
    white-space: nowrap;
  }
  .brand__tagline {
    display: block;
    font-weight: 700;
    white-space: nowrap;
    color: var(--blue-mist);
  }
  .card--front .brand { left: 60px; top: 193px; }
  .card--front .brand__name { font-size: 40px; }
  .card--front .brand__tagline { font-size: 12.5px; margin-top: 8px; }
  .card--back .brand { left: 47px; top: 80px; }
  .card--back .brand__name { font-size: 19px; }
  .card--back .brand__tagline { font-size: 6.2px; margin-top: 4px; }
  .services {
    position: absolute;
    left: 263px;
    top: 72px;
    margin: 0;
    padding: 0;
    list-style: none;
    font-weight: 700;
    font-size: 15px;
    line-height: 21px;
    letter-spacing: 0.2px;
    white-space: nowrap;
  }
  .services li::before {
    content: "• ";
    font-weight: 600;
    color: var(--blue-soft);
  }
  .contact-rule {
    position: absolute;
    left: 252px;
    top: 230px;
    width: 291px;
    height: 1px;
    background: var(--rule);
  }
  .contact {
    position: absolute;
    left: 263px;
    top: 238px;
    margin: 0;
    font-style: normal;
    font-weight: 700;
    font-size: 11.5px;
    line-height: 18px;
    white-space: nowrap;
  }
  .contact span { display: block; }
  .contact__name { color: var(--blue-pale); }
</style>
</head>
<body>
<main class="canvas">

  <section class="card card--front" aria-label="Business card front">
    <svg class="card__sheen" viewBox="0 0 837 474" preserveAspectRatio="none" aria-hidden="true">
      <defs>
        <linearGradient id="front-sheen-a" x1="0.45" y1="0" x2="0.9" y2="0.75">
          <stop offset="0" stop-color="#7BADD7"/>
          <stop offset="0.5" stop-color="#0677BA"/>
          <stop offset="1" stop-color="#021a33"/>
        </linearGradient>
        <linearGradient id="front-sheen-b" x1="1" y1="0" x2="0.6" y2="1">
          <stop offset="0" stop-color="#0677BA"/>
          <stop offset="0.45" stop-color="#0054AA"/>
          <stop offset="1" stop-color="#011226"/>
        </linearGradient>
      </defs>
      <path d="M108 0 L837 0 L837 474 L518 474 C610 420 680 360 713 308 C560 150 330 40 108 0 Z" fill="url(#front-sheen-a)"/>
      <path d="M837 0 C835 220 720 390 518 474 L837 474 Z" fill="url(#front-sheen-b)"/>
    </svg>
    <h1 class="brand">
      <span class="brand__name">Buff &amp; Gleam</span>
      <span class="brand__tagline">polished concrete • epoxy coatings flooring</span>
    </h1>
  </section>

  <section class="card card--back" aria-label="Business card back">
    <svg class="card__sheen" viewBox="0 0 837 474" preserveAspectRatio="none" aria-hidden="true">
      <defs>
        <linearGradient id="back-sheen-a" x1="0.6" y1="0" x2="0.2" y2="0.7">
          <stop offset="0" stop-color="#7BADD7"/>
          <stop offset="0.5" stop-color="#0677BA"/>
          <stop offset="1" stop-color="#021a33"/>
        </linearGradient>
        <linearGradient id="back-sheen-b" x1="0" y1="0.2" x2="0.4" y2="1">
          <stop offset="0" stop-color="#0677BA"/>
          <stop offset="0.5" stop-color="#0054AA"/>
          <stop offset="1" stop-color="#011226"/>
        </linearGradient>
      </defs>
      <path d="M0 0 L728 0 C440 80 230 200 123 310 C60 240 15 130 0 20 Z" fill="url(#back-sheen-a)"/>
      <path d="M0 20 C15 200 130 390 323 474 L0 474 Z" fill="url(#back-sheen-b)"/>
    </svg>
    <h2 class="brand">
      <span class="brand__name">Buff &amp; Gleam</span>
      <span class="brand__tagline">polished concrete • epoxy coatings flooring</span>
    </h2>
    <ul class="services">
      <li>POLISHED CONCRETE</li>
      <li>EPOXY COATING</li>
      <li>TERRAZZO RESTORATION</li>
      <li>SHOT BLASTING</li>
      <li>SURFACE PREPARATION</li>
      <li>JOINT FILLING</li>
      <li>TILE/ CARPET /GLUE REMOVAL</li>
    </ul>
    <div class="contact-rule"></div>
    <address class="contact">
      <span class="contact__name">Ray Tulvin · 586-700-3926</span>
      <span class="contact__email">buffandgleamfloors@mailbrook.example</span>
      <span class="contact__address">47215 Tallowmere Rd, Fraser, MI 48093</span>
      <span class="contact__web">buffandgleamfloors.example</span>
    </address>
  </section>

</main>
</body>
</html>
```